Figure for a research paper

I am working on designing a figure for a research paper that illustrates the effect of KORA Pathway assessment on student outcomes over time by impacting teacher bias and teacher perception of student growth. I built the attached figure via powerpoint. It includes the very basic elements but it does not look great and I am not sure that it is clearly depicting what I am hoping to illustrate. I would like for you to build an illustration of this idea that i can include in the paper.

```html
<!DOCTYPE html>
<html lang="en">
<head>
<meta charset="utf-8">
<title>Effect of KORA Pathway Assessment on SEL Program Effectiveness</title>
<link href="https://fonts.googleapis.com/css2?family=Source+Serif+4:opsz,wght@8..60,600;8..60,700&display=swap" rel="stylesheet">
<style>
  :root {
    --paper: #ffffff;
    --axis-blue: #1a5f80;
    --assessed-red: #e60000;
    --ink: #1a1a1a;
    --muted: #555555;
  }
  html, body {
    margin: 0;
    padding: 0;
    width: 1059px;
    height: 1200px;
    overflow: hidden;
    background: var(--paper);
  }
  .figure { display: block; width: 1059px; height: 1200px; }
  .axis { stroke: var(--axis-blue); stroke-width: 8; fill: none; }
  .trend-baseline { stroke: var(--axis-blue); stroke-width: 7; fill: none; stroke-linecap: round; }
  .trend-assessed { stroke: var(--assessed-red); stroke-width: 7; fill: none; stroke-linecap: round; }
  .gap-marker { stroke: var(--muted); stroke-width: 3; stroke-dasharray: 10 8; fill: none; }
  .pointer-shaft { stroke: var(--ink); stroke-width: 4; }
  .pointer-head { fill: var(--ink); }
  .lift-shaft { stroke: var(--assessed-red); stroke-width: 5; }
  .lift-head { fill: var(--assessed-red); }
  .annotation {
    font-family: "Source Serif 4", Georgia, serif;
    font-weight: 600;
    font-size: 28px;
    fill: var(--ink);
    text-anchor: middle;
  }
  .annotation-lift { fill: var(--assessed-red); }
  .line-label {
    font-family: "Source Serif 4", Georgia, serif;
    font-weight: 700;
    font-size: 28px;
    text-anchor: start;
  }
  .line-label-assessed { fill: var(--assessed-red); }
  .line-label-baseline { fill: var(--axis-blue); }
  .axis-title {
    font-family: "Source Serif 4", Georgia, serif;
    font-weight: 700;
    font-size: 36px;
    fill: var(--ink);
    text-anchor: middle;
  }
  .panel-title {
    font-family: "Source Serif 4", Georgia, serif;
    font-weight: 700;
    font-size: 38px;
    fill: var(--ink);
    text-anchor: start;
  }
</style>
</head>
<body>
<svg class="figure" viewBox="0 0 1800 2040" role="img" aria-label="Two line charts of SEL program effectiveness over time, with and without KORA Pathway assessment">
  <!-- Panel A: with assessment -->
  <g class="chart chart-with-assessment">
    <text class="panel-title" x="323" y="118">A. With KORA Pathway Assessment</text>
    <path class="axis" d="M323 160 V835 H1582"/>
    <line class="trend-baseline" x1="385" y1="785" x2="1495" y2="703"/>
    <line class="trend-assessed" x1="385" y1="785" x2="1490" y2="453"/>
    <line class="gap-marker" x1="1525" y1="462" x2="1525" y2="694"/>

    <text class="line-label line-label-assessed" x="1508" y="440">With assessment</text>
    <text class="line-label line-label-baseline" x="1508" y="745">Baseline</text>

    <text class="axis-title" transform="translate(252 497) rotate(-90)">Effectiveness of SEL Program</text>
    <text class="axis-title" transform="translate(288 497) rotate(-90)">on the Student</text>
    <text class="axis-title" x="953" y="893">Time</text>

    <text class="annotation" x="673" y="565">Teacher Bias</text>
    <line class="pointer-shaft" x1="673" y1="582" x2="673" y2="650"/>
    <polygon class="pointer-head" points="660,646 686,646 673,672"/>

    <text class="annotation" x="1163" y="402">Teacher’s inaccurate perception of</text>
    <text class="annotation" x="1163" y="432">student growth or learning</text>
    <line class="pointer-shaft" x1="1165" y1="445" x2="1165" y2="510"/>
    <polygon class="pointer-head" points="1152,506 1178,506 1165,532"/>

    <line class="lift-shaft" x1="1317" y1="623" x2="1317" y2="560"/>
    <polygon class="lift-head" points="1303,564 1331,564 1317,536"/>
    <text class="annotation annotation-lift" x="1313" y="655">KORA Pathway Assessment</text>
  </g>

  <!-- Panel B: without assessment -->
  <g class="chart chart-without-assessment">
    <text class="panel-title" x="323" y="1096">B. Without KORA Pathway Assessment</text>
    <path class="axis" d="M323 1138 V1813 H1582"/>
    <line class="trend-baseline" x1="323" y1="1632" x2="1490" y2="1430"/>

    <text class="line-label line-label-baseline" x="1508" y="1438">Baseline</text>

    <text class="axis-title" transform="translate(252 1475) rotate(-90)">Effectiveness of SEL Program</text>
    <text class="axis-title" transform="translate(288 1475) rotate(-90)">on the Student</text>
    <text class="axis-title" x="953" y="1872">Time</text>

    <text class="annotation" x="673" y="1436">Teacher Bias</text>
    <line class="pointer-shaft" x1="673" y1="1452" x2="673" y2="1520"/>
    <polygon class="pointer-head" points="660,1516 686,1516 673,1542"/>

    <text class="annotation" x="1163" y="1330">Teacher’s inaccurate perception of</text>
    <text class="annotation" x="1163" y="1360">student growth or learning</text>
    <line class="pointer-shaft" x1="1165" y1="1373" x2="1165" y2="1438"/>
    <polygon class="pointer-head" points="1152,1434 1178,1434 1165,1460"/>
  </g>
</svg>
</body>
</html>
```